Book Cover Design - Uncovering Weight Loss Secrets

I need a book cover design for a book called 'Folding The Map'. It is a book that goes through all of the secrets to weight loss, without any crazy shakes or workouts or pills or potions. The book is really focused on helping people understand that Weight loss is simple and has more to do with our mindset as well as the food we were eating. It is about taking personal responsibility not looking for the next fancy revolutionary product that is going to help them magically melt the fat away. The book is pragmatic in nature and breaks down in simple terms how we can lose weight and keep it off for the rest of our lives. It shows the user that it is simple to lose weight, but it takes effort. They should stop looking for a quick fix when it comes to weight loss but instead eat healthy for the rest of their lives.
The book is intended to be hard-hitting no holds barred approach. The book has the same title as my business name. I will attach the current logo that we use in the business. This doesn't need to be on the front of the book maybe at the back down the bottom somewhere.
I am looking to have both an e-book cover and a standard printed book cover.
I don't have any colours in mind, my logo can be adapted to be different colours or just white.
The message that I am wanting people to feel when they see my book, is that all these Weightloss fads are a joke, that I know the secrets that will get them to their weight loss goal even if they fail at everything else before.
On the cover it should say the following.
FOLDING THE MAP
Uncovering the Weight Loss Secrets
The big companies have been trying to keep hidden for years!
COLIN MAYHEW
People who have failed many times trying to lose weight & need help
Weight Loss

```html
<!DOCTYPE html>
<html lang="en">
<head>
<meta charset="utf-8">
<title>Folding The Map — Book Cover</title>
<link href="https://fonts.googleapis.com/css2?family=Arimo:wght@400;700&display=swap" rel="stylesheet">
<style>
  :root {
    --backdrop: #4a4a4a;
    --paper: #ffffff;
    --ink: #000000;
    --accent: #ffe000;
    --accent-deep: #e8b800;
    --light: #ffffff;
  }
  html, body {
    margin: 0;
    width: 1200px;
    height: 1200px;
    overflow: hidden;
    background: var(--backdrop);
  }
  .cover {
    position: absolute;
    left: 229px;
    top: 38px;
    width: 752px;
    height: 1114px;
    background: var(--paper);
    overflow: hidden;
    font-family: "Arimo", Arial, sans-serif;
  }
  .hero-art {
    position: absolute;
    left: 0;
    top: 100px;
    width: 752px;
    height: 578px;
  }
  .kicker {
    position: absolute;
    left: 0;
    right: 0;
    top: 48px;
    text-align: center;
    color: var(--ink);
    font-weight: 700;
    line-height: 1;
  }
  .kicker-lead { display: block; font-size: 60px; letter-spacing: 1px; }
  .kicker-sub { display: block; font-size: 33px; margin-top: 8px; }
  .kicker-sub + .kicker-sub { margin-top: 5px; }
  .title-band {
    position: absolute;
    left: 0;
    top: 677px;
    width: 752px;
    height: 360px;
    background: var(--ink);
  }
  .title-main {
    position: absolute;
    left: 0;
    right: 0;
    top: 700px;
    text-align: center;
    color: var(--accent);
    font-weight: 700;
    font-size: 122px;
    line-height: 1;
    letter-spacing: 1px;
  }
  .title-second {
    position: absolute;
    left: 0;
    right: 0;
    top: 808px;
    text-align: center;
    color: var(--light);
    font-weight: 700;
    line-height: 1;
  }
  .title-second .small { font-size: 58px; margin-right: 12px; }
  .title-second .large { font-size: 150px; }
  .tagline {
    position: absolute;
    left: 0;
    right: 0;
    top: 950px;
    text-align: center;
    color: var(--light);
    font-size: 27px;
    line-height: 37px;
  }
  .author-band {
    position: absolute;
    left: 0;
    top: 1037px;
    width: 752px;
    height: 77px;
    display: flex;
    align-items: center;
    justify-content: center;
    color: var(--ink);
    font-weight: 700;
    font-size: 52px;
    letter-spacing: 1px;
  }
</style>
</head>
<body>
  <div class="cover">
    <svg class="hero-art" viewBox="0 0 752 578" role="img" aria-label="Yellow tape measure opening like a zipper over a dark body silhouette">
      <defs>
        <linearGradient id="tapeTone" x1="0" y1="0" x2="0" y2="1">
          <stop offset="0" stop-color="var(--accent)"/>
          <stop offset="0.55" stop-color="var(--accent-deep)"/>
          <stop offset="1" stop-color="#3a3000"/>
        </linearGradient>
      </defs>
      <path d="M0 10 L372 330 L752 0 L752 578 L0 578 Z" fill="url(#tapeTone)"/>
    </svg>

    <div class="kicker">
      <span class="kicker-lead">UNCOVERING</span>
      <span class="kicker-sub">THE WEIGHT LOSS</span>
      <span class="kicker-sub">SECRETS</span>
    </div>

    <div class="title-band"></div>
    <div class="title-main">FOLDING</div>
    <div class="title-second"><span class="small">THE</span><span class="large">MAP</span></div>
    <div class="tagline">THE BIG COMPANIES HAVE BEEN TRYING<br>TO KEEP HIDDEN FOR YEARS!</div>

    <div class="author-band">COLIN MAYHEW</div>
  </div>
</body>
</html>
```